Awesome Flyer for Tactical Emergency Response Services

We need a Flyer for Emergency Rapid Response services for my company ferncrest Security Services Ltd. , we are a security guisard service based in Trinidad in the Caribbean.
The flyer will include price and pictures of our tactical team. must be clear concise, and strong.

Rapid response services is where customers pay a monthly fee and if they have any security issues they call us and we immediately respond to their home or business to ensure their safety and security.

Target Market(s)

Homeowners; people worried about home security such as home invasions etc.

Requirements
Must have
• Company Logo prominent

```html
<!DOCTYPE html>
<html lang="en">
<head>
<meta charset="utf-8">
<title>Ferncrest Security Services – 24 HR Emergency Rapid Response</title>
<link rel="stylesheet" href="https://fonts.googleapis.com/css2?family=Montserrat:wght@400;600;700;800&display=swap">
<style>
  :root {
    --stage: #9a9a9a;
    --red: #c5262d;
    --red-deep: #9e1419;
    --ink: #231f20;
    --grey-light: #c9c9c9;
    --grey-mid: #8e8e8e;
    --white: #ffffff;
  }
  html, body {
    margin: 0;
    width: 1200px;
    height: 1126px;
    overflow: hidden;
    background: var(--stage);
  }
  .flyer-canvas {
    display: block;
    width: 1200px;
    height: 1126px;
    font-family: "Montserrat", sans-serif;
  }
  .headline { font-weight: 800; font-size: 44px; fill: var(--white); }
  .subhead { font-weight: 700; font-size: 26px; fill: var(--white); }
  .lead { font-weight: 400; font-size: 15.5px; fill: var(--white); }
  .offer-value { font-weight: 700; font-size: 56px; fill: var(--white); }
  .offer-label { font-weight: 700; font-size: 17px; fill: var(--white); }
  .brand-name { font-weight: 600; font-size: 15px; fill: var(--white); letter-spacing: 0.5px; }
  .info-title { font-weight: 400; font-size: 11px; fill: var(--white); }
  .info-body { font-weight: 400; font-size: 7px; fill: var(--white); }
  .info-tiny { font-weight: 400; font-size: 5px; fill: var(--white); }
  .contact { font-weight: 700; font-size: 8.5px; fill: var(--white); }
</style>
</head>
<body>
<svg class="flyer-canvas" viewBox="0 0 1386 1300" preserveAspectRatio="none" xmlns="http://www.w3.org/2000/svg">
  <defs>
    <linearGradient id="topShade" x1="0" y1="0" x2="1" y2="0">
      <stop offset="0" stop-color="#4a4a4a"/>
      <stop offset="1" stop-color="#1a1718"/>
    </linearGradient>
    <linearGradient id="greyPanel" x1="0" y1="0" x2="0" y2="1">
      <stop offset="0" stop-color="#6d6d6d"/>
      <stop offset="1" stop-color="#d0d0d0"/>
    </linearGradient>
    <linearGradient id="redField" x1="0" y1="0" x2="1" y2="0">
      <stop offset="0" stop-color="#a8181e"/>
      <stop offset="1" stop-color="#c8262d"/>
    </linearGradient>
    <linearGradient id="darkBand" x1="0" y1="0" x2="1" y2="0">
      <stop offset="0" stop-color="#231f20"/>
      <stop offset="0.45" stop-color="#231f20" stop-opacity="0.85"/>
      <stop offset="1" stop-color="#231f20" stop-opacity="0"/>
    </linearGradient>
    <linearGradient id="photoTone" x1="0" y1="0" x2="0" y2="1">
      <stop offset="0" stop-color="#e6e8e6"/>
      <stop offset="0.25" stop-color="#5e7a4a"/>
      <stop offset="0.45" stop-color="#9a9a94"/>
      <stop offset="0.7" stop-color="#3f5a2c"/>
      <stop offset="1" stop-color="#4f7a2e"/>
    </linearGradient>
    <linearGradient id="infoBox" x1="0" y1="0" x2="1" y2="0">
      <stop offset="0" stop-color="#c5262d" stop-opacity="0"/>
      <stop offset="1" stop-color="#8e0f14"/>
    </linearGradient>
    <clipPath id="flyerClip"><rect x="293" y="87" width="800" height="1125"/></clipPath>
  </defs>

  <g class="flyer" clip-path="url(#flyerClip)">
    <rect class="flyer-base" x="293" y="87" width="800" height="1125" fill="url(#topShade)"/>
    <polygon class="side-panel" points="980,128 1093,112 1093,520 1020,520" fill="url(#greyPanel)"/>

    <rect class="team-photo" x="293" y="517" width="800" height="695" fill="url(#photoTone)"
          role="img" aria-label="Photo of the tactical response team detaining a suspect beside a marked patrol vehicle"/>

    <polygon class="red-field" points="293,215 990,125 1035,555 525,662 293,905" fill="url(#redField)"/>
    <rect class="headline-band" x="293" y="247" width="800" height="201" fill="url(#darkBand)"/>

    <g class="accent-bars">
      <rect x="500" y="598" width="500" height="26" rx="13" fill="var(--grey-mid)" transform="rotate(-9 750 611)"/>
      <rect x="490" y="585" width="490" height="18" rx="9" fill="var(--white)" transform="rotate(-9 735 594)"/>
      <polygon points="860,1000 1093,978 1093,988 860,1010" fill="var(--ink)"/>
      <polygon points="860,1040 1093,1016 1093,1022 860,1046" fill="var(--grey-mid)"/>
    </g>

    <g class="brand">
      <circle cx="400" cy="150" r="26" fill="var(--white)"/>
      <text class="brand-name" x="324" y="212">FERNCREST</text>
      <text class="brand-name" x="324" y="234">SECURITY SERVICES</text>
    </g>

    <text class="headline" x="372" y="348">24 HR EMERGENCY</text>
    <text class="headline" x="372" y="402">RAPID RESPONSE</text>

    <text class="subhead" x="350" y="496">Lorem ipsum</text>
    <text class="lead" x="353" y="531">Lorem ipsum dolor sit amet, consectetuer adipiscing elit, sed diam nonu</text>

    <g class="offer-badge">
      <circle cx="424" cy="674" r="103" fill="var(--red)"/>
      <text class="offer-value" x="422" y="682" text-anchor="middle">20%</text>
      <text class="offer-label" x="424" y="702" text-anchor="middle">LOREM IPSUM</text>
    </g>

    <g class="contact-corner">
      <polygon points="800,1212 860,1065 1093,1020 1093,1212" fill="var(--red)"/>
      <rect x="930" y="1062" width="163" height="103" fill="url(#infoBox)"/>
      <text class="info-title" x="1015" y="1075" text-anchor="end">LOREM IPSUN</text>
      <text class="info-body" x="1015" y="1089" text-anchor="end">Loremipsumdolorsitamet,</text>
      <text class="info-body" x="1015" y="1098" text-anchor="end">consectetuer adipiscing</text>
      <text class="info-body" x="1015" y="1107" text-anchor="end">elit, sed diam nonummy</text>
      <text class="info-tiny" x="1015" y="1122" text-anchor="end">Lorem ipsum dolor sit</text>
      <text class="info-tiny" x="1015" y="1129" text-anchor="end">amet, consectetuer</text>
      <circle cx="985" cy="1137" r="3.5" fill="var(--white)"/>
      <circle cx="997" cy="1137" r="3.5" fill="var(--white)"/>
      <circle cx="1009" cy="1137" r="3.5" fill="var(--white)"/>
      <text class="contact" x="1017" y="1162" text-anchor="end">Contact:</text>
      <text class="contact" x="1017" y="1175" text-anchor="end">Tel: 290-0418 / 290-0427</text>
      <text class="contact" x="1017" y="1188" text-anchor="end">email: info@ferncrest-tt.com</text>
    </g>
  </g>
</svg>
</body>
</html>
```